Cloud backup company needs a new website

We need a new design for our website as the current one is quite dated now. You can view the current website at www.vellostrand-files.net.au to view the content elements.

We provide cloud backup services (ie remote off site to a cluster of servers) to small to medium businesses looking for better alternatives to tape or optical media backups.

Target Market(s)

SME/SMB (Businesses with fewer than 100 employees)

Industry/Entity Type

It Company

Requirements
Must have
• Must have sections to sign up to newsletter, log in to account, view news feed as per current website.

Must have a prominent call to action to sign up for a trial and view pricing.

Also like it to have twitter and facebook links/likes integration
Should not have
• No Flash, no serif fonts

```html
<!DOCTYPE html>
<html lang="en">
<head>
<meta charset="utf-8">
<title>vellostrand – Cloud Backup</title>
<link href="https://fonts.googleapis.com/css2?family=Mako&family=PT+Sans:ital,wght@0,400;0,700;1,400&display=swap" rel="stylesheet">
<style>
:root{
  --orange:#ef6a1c;
  --orange-dark:#d85a12;
  --ink:#333333;
  --charcoal:#2a2a2c;
  --slogan:#363030;
  --page:#f1f1f1;
  --white:#ffffff;
  --footer-link:#ffd3b3;
}
*{margin:0;padding:0;box-sizing:border-box}
html,body{width:766px;height:1200px;overflow:hidden}
body{position:relative;background:var(--page);font-family:'PT Sans',Arial,sans-serif;color:var(--ink)}
.abs{position:absolute}
.orange-field{left:0;top:865px;width:766px;height:335px;background:var(--orange)}
.brand-block{left:77px;top:0;width:200px;height:83px;background:var(--white)}
.brand-name{left:79px;top:24px;font-size:33px;font-weight:400;color:var(--orange);letter-spacing:-0.5px}
.utility{left:557px;top:9px;font-size:8px;color:#555}
.utility-phone{left:655px;top:9px;font-size:8px;font-weight:700;color:#555}
.search{left:468px;top:41px;width:218px;height:21px;background:var(--white);border:1px solid #e2e2e2;font-size:10px;color:#b5b5b5;padding:4px 14px}
.search-icon{left:694px;top:41px}
.main-nav{left:77px;top:83px;width:626px;height:30px;background:var(--orange);display:flex}
.main-nav span{color:var(--white);font-size:10px;font-weight:700;line-height:30px;text-align:center;border-right:1px solid #f58a4a}
.social{top:87px;width:21px;height:21px;border-radius:3px}
.social.one{left:651px;background:#3b5a8f}
.social.two{left:675px;background:#33a8d9}
.content-panel{left:82px;top:113px;width:626px;height:860px;background:var(--white)}
.hero{left:89px;top:133px;width:421px;height:172px;background:radial-gradient(ellipse at 45% 55%,#f8a32a,#c4400c 55%,#3a1505)}
.hero-side{left:510px;top:133px;width:179px;height:199px;background:linear-gradient(#3a2a20,#1e1a18);color:var(--white);padding:22px 16px}
.hero-side h2{font-size:15px;font-weight:400;line-height:19px;margin-bottom:10px}
.hero-side p{font-size:6.5px;line-height:10.5px;color:#d8d8d8}
.hero-side a{display:block;margin-top:12px;font-size:7px;color:var(--white);text-decoration:underline}
.hero-caption{left:89px;top:305px;width:421px;height:27px;background:#2b2522;color:var(--white);padding:7px 11px;font-size:11px;white-space:nowrap}
.hero-caption small{font-size:7px;color:#ccc;margin-left:4px}
.dots{left:270px;top:291px;display:flex;gap:9px}
.dots i{width:5px;height:5px;border-radius:50%;background:#eee;display:block}
.cta{left:77px;top:332px;width:626px;height:43px;background:var(--orange);overflow:hidden}
.cta-label{left:116px;top:331px;color:var(--white);font-size:45px;line-height:45px;letter-spacing:0.5px;white-space:nowrap}
.cta-phone{left:405px;top:336px;color:var(--white);font-size:34px;line-height:36px;font-weight:700;white-space:nowrap}
.trial-bar{left:85px;top:381px;width:425px;height:70px;background:var(--charcoal)}
.trial-tab{left:85px;top:381px;width:67px;height:70px;background:var(--orange);border-left:4px solid #f4a623}
.trial-label{left:91px;top:445px;transform:rotate(-90deg);transform-origin:0 0;color:var(--white);font-size:17px;line-height:16px;width:60px;text-align:center}
.newsletter-input{left:163px;top:389px;width:264px;height:16px;background:var(--white)}
.sub-item{top:422px;font-size:20px;line-height:26px;color:var(--white);white-space:nowrap}
.sub-active{left:345px;top:422px;width:75px;height:30px;background:var(--orange)}
.active-tip{left:345px;top:451px}
.login{left:533px;top:380px;width:157px;height:153px;background:var(--charcoal);border-radius:8px 8px 0 0}
.login-title{left:542px;top:411px;font-size:11px;color:var(--white)}
.field{left:558px;width:115px;height:16px;background:var(--white)}
.btn{top:477px;width:65px;height:18px;background:var(--orange);color:var(--white);font-size:11px;font-weight:700;text-align:center;line-height:18px}
.radio{left:543px;font-size:11px;color:var(--white);display:flex;align-items:center;gap:11px}
.radio i{width:9px;height:9px;border-radius:50%;border:2px solid #ddd;display:block}
.slogan-panel{left:541px;top:537px;width:146px;height:321px;background:linear-gradient(#3d3636,var(--slogan))}
.section-icon{width:32px;height:32px;border-radius:50%;background:var(--orange)}
.section-title{font-size:19px;font-weight:400;color:#222}
.copy{left:97px;font-family:'Mako',sans-serif;font-size:13px;line-height:14.5px;color:#333;letter-spacing:0.45px;white-space:nowrap}
.video{left:96px;top:567px;width:403px;height:160px;background:linear-gradient(100deg,#3b2a20,#6b5b55 40%,#2f3f5a 70%,#1d2438)}
.news-thumb{top:823px;width:36px;height:36px;background:#000}
.news-item{top:824px;width:135px;font-size:7px;line-height:9px;color:#333}
.news-item h4{color:var(--orange);font-size:7.5px;font-weight:400}
.news-item em{display:block;color:#aaa;font-size:6px;margin:2px 0 4px}
.carousel-img{top:888px;width:87px;height:70px}
.arrow-btn{top:918px;width:12px;height:12px;border-radius:50%;background:#777}
.footer-rule{left:77px;top:982px;width:626px;height:1px;background:#f7b48a}
.footer-col{top:1008px;color:var(--white)}
.footer-col h3{font-size:11px;font-weight:400;margin-bottom:9px}
.footer-col li{list-style:none;font-size:7px;color:var(--footer-link);height:17.7px;padding-left:14px;position:relative}
.footer-col li::before{content:"→";position:absolute;left:0;color:var(--white);font-size:7px}
.bottom-rule{left:89px;top:1128px;width:600px;height:1px;background:#c9540f}
.copyright{left:89px;top:1141px;font-size:7px;font-style:italic;color:var(--white)}
</style>
</head>
<body>

<div class="abs orange-field"></div>

<header>
  <div class="abs brand-block"></div>
  <div class="abs brand-name">vellostrand</div>
  <div class="abs utility">News | Pricelist| Call</div>
  <svg class="abs" style="left:643px;top:9px" width="7" height="9" viewBox="0 0 7 9"><circle cx="3.5" cy="2.2" r="2" fill="#777"/><path d="M0 9 Q3.5 3 7 9Z" fill="#777"/></svg>
  <div class="abs utility-phone">1300 462 715</div>
  <div class="abs search">Type your keywords...</div>
  <svg class="abs search-icon" width="16" height="18" viewBox="0 0 16 18"><circle cx="7" cy="7" r="5.5" fill="none" stroke="#fff" stroke-width="2"/><line x1="11" y1="11" x2="15" y2="16" stroke="#fff" stroke-width="2.5"/></svg>

  <nav class="abs main-nav">
    <span style="width:62px">Home</span>
    <span style="width:62px">Solutions</span>
    <span style="width:74px">Services</span>
    <span style="width:75px">Support</span>
    <span style="width:81px">Partners</span>
    <span style="width:69px">About</span>
    <span style="width:63px">Download</span>
  </nav>
  <div class="abs social one" aria-label="Social link"></div>
  <div class="abs social two" aria-label="Social link"></div>
</header>

<main>
  <div class="abs content-panel"></div>

  <section>
    <div class="abs hero" role="img" aria-label="Hard drive engulfed in flames with the word FIRE"></div>
    <div class="abs dots"><i></i><i></i><i></i></div>
    <div class="abs hero-side">
      <h2>Adipiscing Sem len Ullamcorper.</h2>
      <p>Curabitur blandit tempus porttitor. Donec ullamcorper nulla non metus auctor fringilla. Nullam quis risus eget urna mollis ornare vel eu leo. Cras justo odio, dapibus ut facilisis in, egestas eget quam.</p>
      <a>Read More</a>
    </div>
    <div class="abs hero-caption">Adipiscing Sem Ullamcorper <small>Curabitur blandit tempus porttitor. Donec ullamcorper nulla non metus auctor fringilla.</small></div>
  </section>

  <div class="abs cta"></div>
  <div class="abs cta-label">Call to Action</div>
  <div class="abs cta-phone">1300 462 715</div>

  <section>
    <div class="abs trial-bar"></div>
    <div class="abs trial-tab"></div>
    <div class="abs trial-label">Trial<br>for<br>FREE</div>
    <div class="abs newsletter-input"></div>
    <svg class="abs" style="left:436px;top:391px" width="20" height="13" viewBox="0 0 20 13"><rect x="0.5" y="0.5" width="19" height="12" fill="none" stroke="#fff"/><path d="M0.5 0.5 L10 7 L19.5 0.5 M0.5 12.5 L7.5 5.5 M19.5 12.5 L12.5 5.5" fill="none" stroke="#fff"/></svg>
    <svg class="abs" style="left:455px;top:364px" width="72" height="72" viewBox="0 0 72 72"><path d="M6 0 L28 0 L72 44 L72 66 Z" fill="var(--orange)"/><text x="39" y="33" transform="rotate(45 39 33)" font-size="12" fill="#fff" text-anchor="middle" dominant-baseline="middle" font-family="PT Sans, sans-serif">Sign up</text></svg>
    <div class="abs sub-active"></div>
    <svg class="abs active-tip" width="75" height="9" viewBox="0 0 75 9"><path d="M0 0 H75 L37.5 9 Z" fill="var(--orange)"/></svg>
    <div class="abs sub-item" style="left:160px">Newsletter</div>
    <div class="abs sub-item" style="left:264px">Services</div>
    <div class="abs sub-item" style="left:348px">Support</div>
    <div class="abs sub-item" style="left:432px">Contact</div>
  </section>

  <section>
    <div class="abs login"></div>
    <svg class="abs" style="left:636px;top:375px" width="58" height="58" viewBox="0 0 58 58"><path d="M4 0 L24 0 L58 34 L58 54 Z" fill="var(--orange)"/><text x="33" y="21" transform="rotate(45 33 21)" font-size="11" fill="#fff" text-anchor="middle" dominant-baseline="middle" font-family="PT Sans, sans-serif">Login</text></svg>
    <div class="abs login-title">Sign in</div>
    <svg class="abs" style="left:543px;top:431px" width="10" height="11" viewBox="0 0 10 11"><circle cx="5" cy="3" r="2.6" fill="#fff"/><path d="M0 11 Q5 3 10 11Z" fill="#fff"/></svg>
    <div class="abs field" style="top:428px"></div>
    <svg class="abs" style="left:543px;top:454px" width="10" height="12" viewBox="0 0 10 12"><path d="M2.5 5 V3.5 a2.5 2.5 0 0 1 5 0 V5" fill="none" stroke="#fff" stroke-width="1.5"/><rect x="0.5" y="5" width="9" height="7" fill="#fff"/></svg>
    <div class="abs field" style="top:452px"></div>
    <div class="abs btn" style="left:545px">Sign up</div>
    <div class="abs btn" style="left:614px">Ok</div>
    <div class="abs radio" style="top:503px"><i></i>Create new account</div>
    <div class="abs radio" style="top:515px"><i style="background:#5d8fc9"></i>Request new password</div>
  </section>

  <div class="abs slogan-panel" role="img" aria-label="Bold stacked lettering poster urging visitors to protect their business data"></div>

  <section>
    <div class="abs section-icon" style="left:96px;top:462px"></div>
    <svg class="abs" style="left:104px;top:470px" width="16" height="16" viewBox="0 0 16 16"><path d="M8 1 L10 6 L15 6 L11 9.5 L12.5 15 L8 11.5 L3.5 15 L5 9.5 L1 6 L6 6 Z" fill="#fff"/></svg>
    <h2 class="abs section-title" style="left:138px;top:466px">About us</h2>
    <p class="abs copy" style="top:500px">Morbi leo risus, porta ac consectetur ac, vestibulum at<br>estibulum id ligula porta felis euismod semper.Nulla vite<br>libero, a pharetra augue. Donec ullamcorper nulla nonu<br>s auctor fringilla.</p>
    <div class="abs video" role="img" aria-label="Crashed hard drive beside a screen full of error messages, video still"></div>
    <svg class="abs" style="left:272px;top:630px" width="44" height="44" viewBox="0 0 44 44"><circle cx="22" cy="22" r="21" fill="#fff" fill-opacity="0.35"/><path d="M17 13 L31 22 L17 31 Z" fill="#fff" fill-opacity="0.6"/></svg>
    <p class="abs copy" style="top:746px">Morbi leo risus, porta ac consectetur ac, vestibulum at<br>estibulum id ligula porta felis euismod semper.Nulla vite<br>libero, a pharetra augue. Donec ullamcorper nulla nonu<br>s auctor fringilla.</p>
  </section>

  <section>
    <div class="abs section-icon" style="left:96px;top:822px;width:30px;height:30px"></div>
    <svg class="abs" style="left:103px;top:830px" width="16" height="14" viewBox="0 0 16 14"><path d="M1 4 H4 L8 1 V13 L4 10 H1 Z" fill="#fff"/><path d="M10.5 4 Q12.5 7 10.5 10 M12.5 2 Q16 7 12.5 12" fill="none" stroke="#fff" stroke-width="1.3"/></svg>
    <h2 class="abs section-title" style="left:132px;top:827px;font-size:16px">News</h2>
    <div class="abs news-thumb" style="left:183px"></div>
    <div class="abs news-item" style="left:228px"><h4>Aenean Lorem Fringilla</h4><em>Posted on 12 Jul 2012</em>Lorem ipsum dolor sit amet, consectetur adipiscing elit. e dapibus, tellus ac.</div>
    <div class="abs news-thumb" style="left:363px"></div>
    <div class="abs news-item" style="left:408px"><h4>Condimentum Fusce Venenatis</h4><em>Posted on 12 Jul 2012</em>Lorem ipsum dolor sit amet,</div>
  </section>

  <section>
    <div class="abs arrow-btn" style="left:105px"></div>
    <svg class="abs" style="left:105px;top:918px" width="12" height="12" viewBox="0 0 12 12"><path d="M7 3 L4 6 L7 9" fill="none" stroke="#fff" stroke-width="1.5"/></svg>
    <div class="abs carousel-img" style="left:138px;background:linear-gradient(#f7b020,#d9440e)" role="img" aria-label="Cartoon of a computer on fire"></div>
    <div class="abs carousel-img" style="left:244px;background:linear-gradient(#e8e8e8,#9a9a9a)" role="img" aria-label="Laptop secured with a padlock"></div>
    <div class="abs carousel-img" style="left:350px;background:linear-gradient(#d5dbe2,#7b8590)" role="img" aria-label="Businessman working at a laptop"></div>
    <div class="abs carousel-img" style="left:456px;background:linear-gradient(#5d6e3a,#c46a1c)" role="img" aria-label="Cartoon of an office worker beside a burning computer"></div>
    <div class="abs carousel-img" style="left:556px;background:linear-gradient(#f4f4f4,#c7b39a)" role="img" aria-label="Coffee spilled over a keyboard"></div>
    <div class="abs arrow-btn" style="left:663px"></div>
    <svg class="abs" style="left:663px;top:918px" width="12" height="12" viewBox="0 0 12 12"><path d="M5 3 L8 6 L5 9" fill="none" stroke="#fff" stroke-width="1.5"/></svg>
  </section>
</main>

<footer>
  <div class="abs footer-rule"></div>
  <div class="abs footer-col" style="left:89px"><h3>Our Company</h3><ul><li>About us</li><li>In The Press</li><li>Testimonials</li><li>Site Security</li></ul></div>
  <div class="abs footer-col" style="left:242px"><h3>Our Solutions</h3><ul><li>About us</li><li>In The Press</li><li>Testimonials</li><li>Site Security</li></ul></div>
  <div class="abs footer-col" style="left:396px"><h3>Our Services</h3><ul><li>About us</li><li>In The Press</li><li>Testimonials</li><li>Site Security</li></ul></div>
  <div class="abs footer-col" style="left:549px"><h3>Download</h3><ul><li>About us</li><li>In The Press</li><li>Testimonials</li><li>Site Security</li></ul></div>
  <div class="abs bottom-rule"></div>
  <div class="abs copyright">Copy right 2013 All right reserved &copy; vellostrand</div>
</footer>

</body>
</html>
```